World travel poster - I want to remember where I've been!

I would like a poster for me to print and keep in my home as a record of my world travels. It must look like a mechanical sign in an airport (see picture for example) However I am flexible with exact layout, if you'd like to add images used to enhance poster etc. I have also uploaded some pictures from my travels if you would like to use some or all of them. They are named according to location.

Poster must include:
USA 2003
Malaysia 2006
Thailand 2007
Italy 2009
India, Vietnam, Hong Kong 2010
Bali 2011
Malaysia 2012
Singapore 2012
Vietnam, Cambodia, Laos 2013
Europe 2015

and the quote:

"The world is a book and those who do not travel read only one page."
― Severin of Tallowmere
Updates

Hi there. I have uploaded some photos of my travels to possibly use in my poster. They are named according to location. I haven't decided if I prefer the originial layout or with images, so please post both for me to consider. Thanks so much for your time to consider my project.

Target Market(s)

Something to catch the eye of visitors and remind me of my adventures.
A classic piece that is a conversation starter.

Industry/Entity Type

Airport

Other font styles liked:
• Airport mechanical font

Requirements
Must have
• Some lettering like a mechanical airport board (see image attached for example).
Dimensions that are easy to print - either A3, or a long/narrow poster.
Nice to have
• A splash of colour or an image, maybe the words 'arrivals' or 'departures'

Use of some of my pictures if it doesn't look too busy.
Should not have
• Anything too over the top.

```html
<!DOCTYPE html>
<html lang="en">
<head>
<meta charset="utf-8">
<title>World Travels Poster</title>
<link rel="stylesheet" href="https://fonts.googleapis.com/css2?family=Archivo+Black&family=Share+Tech+Mono&family=Courgette&display=swap">
<style>
:root{
  --bar-top:#3a3a3a;
  --bar-bottom:#050505;
  --sign-yellow:#f7e01a;
  --sign-blue:#2b4fa8;
  --wood-light:#d98f45;
  --wood-mid:#c8772f;
  --wood-dark:#a95d1e;
  --board:#151515;
  --tile:#262626;
  --tile-line:#0a0a0a;
  --flap-text:#f2f2f2;
  --paper:#f2f1e4;
  --paper-shade:#e2e0cf;
  --pin-green:#7cc243;
  --pin-red:#d11f28;
  --polaroid:#fbfbf8;
  --quote-red:#b3121b;
  --quote-glow:#ffd21f;
}
*{box-sizing:border-box;margin:0;padding:0}
html,body{width:1200px;height:900px;overflow:hidden}
body{position:relative;background:
  repeating-linear-gradient(180deg,transparent 0 86px,rgba(90,40,5,.35) 86px 88px),
  linear-gradient(100deg,var(--wood-mid),var(--wood-light) 40%,var(--wood-mid) 70%,var(--wood-dark));
  font-family:"Archivo Black",sans-serif}

.top-bar{position:absolute;left:0;top:0;width:1200px;height:116px;
  background:linear-gradient(var(--bar-top),var(--bar-bottom));box-shadow:0 6px 12px rgba(0,0,0,.5)}
.sign-icon{position:absolute;top:14px;width:84px;height:84px;border:4px solid var(--sign-yellow);border-radius:6px}
.sign-icon svg{width:100%;height:100%}
.sign-icon.arrivals{left:27px}
.sign-icon.departures{left:1086px}
.sign-word{position:absolute;top:28px;color:var(--sign-yellow);font-size:46px;line-height:60px}
.sign-word.arrivals{left:200px}
.sign-word.departures{left:762px}
.arrow-disc{position:absolute;top:12px;width:92px;height:92px;border-radius:50%;background:var(--sign-blue)}
.arrow-disc.up{left:465px}
.arrow-disc.right{left:639px}

.hanging-string{position:absolute;top:116px;width:3px;height:38px;background:#f4f4f4}

.flap-board{position:absolute;left:20px;top:152px;width:338px;height:416px;background:var(--board);
  box-shadow:4px 6px 12px rgba(0,0,0,.55);padding:6px 0 0 16px}
.flap-row{display:flex;height:26.7px;align-items:center}
.flap-year,.flap-place{height:22px;font-family:"Share Tech Mono",monospace;color:var(--flap-text);
  font-size:19px;line-height:22px;letter-spacing:7.3px;padding-left:3px;
  background:repeating-linear-gradient(90deg,var(--tile) 0 17px,var(--tile-line) 17px 19.5px)}
.flap-year{width:82px}
.flap-place{width:216px;margin-left:17px}

.world-map{position:absolute;left:418px;top:143px;width:760px;height:418px;
  background:linear-gradient(135deg,var(--paper),var(--paper-shade));box-shadow:3px 5px 10px rgba(0,0,0,.4)}
.map-art{position:absolute;left:50px;top:40px;width:600px;height:330px;border-radius:40px;
  background:radial-gradient(ellipse at 30% 40%,rgba(232,80,40,.35),transparent 60%),
    radial-gradient(ellipse at 70% 30%,rgba(30,170,160,.35),transparent 60%),
    radial-gradient(ellipse at 55% 70%,rgba(120,180,40,.3),transparent 60%)}
.push-pin{position:absolute;width:22px;height:22px;border-radius:50%;
  background:radial-gradient(circle at 35% 35%,#c6f08e,var(--pin-green) 60%,#3f7a1c)}

.polaroid{position:absolute;background:var(--polaroid);padding:8px 8px 20px;box-shadow:2px 4px 8px rgba(0,0,0,.45)}
.polaroid .photo{width:100%;height:100%}
.polaroid::before{content:"";position:absolute;left:50%;top:-4px;width:8px;height:8px;margin-left:-4px;
  border-radius:50%;background:var(--pin-red)}

.travel-quote{position:absolute;left:18px;top:728px;width:610px;font-family:"Courgette",cursive;
  font-size:35px;line-height:44px;color:var(--quote-red);text-align:center;
  text-shadow:0 0 3px var(--quote-glow),0 0 3px var(--quote-glow),0 0 5px var(--quote-glow),2px 2px 3px rgba(0,0,0,.4)}
.quote-author{position:absolute;left:418px;top:846px;font-family:"Courgette",cursive;font-size:22px;
  color:var(--quote-red);text-shadow:0 0 3px var(--quote-glow),0 0 3px var(--quote-glow)}
</style>
</head>
<body>
<header class="top-bar">
  <div class="sign-icon arrivals">
    <svg viewBox="0 0 76 76" aria-hidden="true"><path d="M10 20 L18 22 L30 36 L52 42 Q60 45 57 50 L20 42 Z M20 20 L26 10 L30 12 L34 36 Z" fill="var(--sign-yellow)"/><rect x="10" y="60" width="56" height="4" fill="var(--sign-yellow)"/></svg>
  </div>
  <div class="sign-word arrivals">Arrivals</div>
  <div class="arrow-disc up"><svg viewBox="0 0 92 92" aria-hidden="true"><path d="M46 16 L72 46 L56 46 L56 76 L36 76 L36 46 L20 46 Z" fill="#fff"/></svg></div>
  <div class="arrow-disc right"><svg viewBox="0 0 92 92" aria-hidden="true"><path d="M76 46 L46 72 L46 56 L16 56 L16 36 L46 36 L46 20 Z" fill="#fff"/></svg></div>
  <div class="sign-word departures">Departures</div>
  <div class="sign-icon departures">
    <svg viewBox="0 0 76 76" aria-hidden="true"><path d="M12 46 L16 40 L28 42 L56 20 Q66 14 66 22 L36 50 Z M34 30 L24 22 L28 19 L44 26 Z" fill="var(--sign-yellow)"/><rect x="10" y="60" width="56" height="4" fill="var(--sign-yellow)"/></svg>
  </div>
</header>

<div class="hanging-string" style="left:55px"></div>
<div class="hanging-string" style="left:328px"></div>

<section class="flap-board" aria-label="Travel history">
  <div class="flap-row"><span class="flap-year">2003</span><span class="flap-place">USA</span></div>
  <div class="flap-row"><span class="flap-year">2006</span><span class="flap-place">MALAYSIA</span></div>
  <div class="flap-row"><span class="flap-year">2007</span><span class="flap-place">THAILAND</span></div>
  <div class="flap-row"><span class="flap-year">2009</span><span class="flap-place">ITALY</span></div>
  <div class="flap-row"><span class="flap-year">2010</span><span class="flap-place">INDIA</span></div>
  <div class="flap-row"><span class="flap-year">2010</span><span class="flap-place">VIETNAM</span></div>
  <div class="flap-row"><span class="flap-year">2010</span><span class="flap-place">HONG KONG</span></div>
  <div class="flap-row"><span class="flap-year">2011</span><span class="flap-place">BALI</span></div>
  <div class="flap-row"><span class="flap-year">2012</span><span class="flap-place">MALAYSIA</span></div>
  <div class="flap-row"><span class="flap-year">2012</span><span class="flap-place">SINGAPORE</span></div>
  <div class="flap-row"><span class="flap-year">2013</span><span class="flap-place">VIETNAM</span></div>
  <div class="flap-row"><span class="flap-year">2013</span><span class="flap-place">CAMBODIA</span></div>
  <div class="flap-row"><span class="flap-year">2013</span><span class="flap-place">LAOS</span></div>
  <div class="flap-row"><span class="flap-year">2015</span><span class="flap-place">EUROPE</span></div>
  <div class="flap-row"><span class="flap-year"></span><span class="flap-place"></span></div>
</section>

<section class="world-map">
  <div class="map-art" role="img" aria-label="Colourful typographic world map with country names forming the continents"></div>
  <span class="push-pin" style="left:10px;top:8px"></span>
  <span class="push-pin" style="left:727px;top:10px"></span>
  <span class="push-pin" style="left:727px;top:395px"></span>
</section>

<div class="polaroid" style="left:1062px;top:182px;width:122px;height:140px;transform:rotate(4deg)"><div class="photo" role="img" aria-label="Travel photo: lighting candles at a temple" style="background:linear-gradient(#5a3a20,#2a1a10)"></div></div>
<div class="polaroid" style="left:383px;top:468px;width:114px;height:122px;transform:rotate(-2deg)"><div class="photo" role="img" aria-label="Travel photo: two friends in a garden" style="background:linear-gradient(#6f8a4a,#3b4a2a)"></div></div>
<div class="polaroid" style="left:342px;top:580px;width:128px;height:114px;transform:rotate(-6deg)"><div class="photo" role="img" aria-label="Travel photo: temple roof in Singapore" style="background:linear-gradient(#9ec4e8,#c49040)"></div></div>
<div class="polaroid" style="left:466px;top:530px;width:110px;height:120px;transform:rotate(6deg)"><div class="photo" role="img" aria-label="Travel photo: market vendor with produce" style="background:linear-gradient(#7a9a5a,#4a5a30)"></div></div>
<div class="polaroid" style="left:587px;top:535px;width:94px;height:70px"><div class="photo" role="img" aria-label="Travel photo: children indoors" style="background:linear-gradient(#c08a6a,#6a4a3a)"></div></div>
<div class="polaroid" style="left:712px;top:535px;width:94px;height:72px"><div class="photo" role="img" aria-label="Travel photo: friends at dinner" style="background:linear-gradient(#b07050,#6a3a2a)"></div></div>
<div class="polaroid" style="left:920px;top:505px;width:120px;height:106px"><div class="photo" role="img" aria-label="Travel photo: tea at a table" style="background:linear-gradient(#a89070,#5a4a3a)"></div></div>
<div class="polaroid" style="left:535px;top:598px;width:116px;height:128px;transform:rotate(-2deg)"><div class="photo" role="img" aria-label="Travel photo: marble mausoleum through an archway" style="background:linear-gradient(#d8e4ee,#3a2a20)"></div></div>
<div class="polaroid" style="left:645px;top:585px;width:106px;height:116px"><div class="photo" role="img" aria-label="Travel photo: large hilltop statue" style="background:linear-gradient(#cfd8e0,#5a6a4a)"></div></div>
<div class="polaroid" style="left:815px;top:574px;width:120px;height:92px;transform:rotate(5deg)"><div class="photo" role="img" aria-label="Travel photo: friends by a river" style="background:linear-gradient(#9ab0c0,#a07060)"></div></div>
<div class="polaroid" style="left:1040px;top:585px;width:112px;height:106px"><div class="photo" role="img" aria-label="Travel photo: three friends in a European town" style="background:linear-gradient(#9ec8ee,#6a6a6a)"></div></div>
<div class="polaroid" style="left:930px;top:625px;width:116px;height:112px;transform:rotate(-7deg)"><div class="photo" role="img" aria-label="Travel photo: friends at an ancient temple" style="background:linear-gradient(#c89070,#4a3a5a)"></div></div>
<div class="polaroid" style="left:726px;top:640px;width:114px;height:120px;transform:rotate(2deg)"><div class="photo" role="img" aria-label="Travel photo: limestone island and longtail boat" style="background:linear-gradient(#7ab8e8,#2f8f9a 60%,#d8c8a0)"></div></div>
<div class="polaroid" style="left:626px;top:710px;width:104px;height:110px"><div class="photo" role="img" aria-label="Travel photo: colourful cliffside village" style="background:linear-gradient(#b0a090,#6a5a50)"></div></div>
<div class="polaroid" style="left:688px;top:755px;width:108px;height:116px"><div class="photo" role="img" aria-label="Travel photo: friends in front of a hotel sign" style="background:linear-gradient(#d8d0c0,#8a5a5a)"></div></div>

<blockquote class="travel-quote">"The world&nbsp; is a book&nbsp; and those who do not travel&nbsp; read only one page."</blockquote>
<p class="quote-author">Severin of Tallowmere</p>
</body>
</html>
```